K7 Maplewave Consulting Group Ltd - Website Design

We already have a company logo. We need a website created for our consulting agency.
Refer to attached files for logo and website content.
We would also be open to any additional recommendations.
Industry/Entity Type
Finance And Accounting
Coding
Coded - Design and coding required
Number of Pages Required
1 page
Font styles to use
Serif
Colors
3377b5
b868aa
33b8a4
Requirements
Must have
- Company Logo, name and who we are.

```html
<!DOCTYPE html>
<html lang="en">
<head>
<meta charset="utf-8">
<title>K7 Maplewave Consulting Group Ltd</title>
<link href="https://fonts.googleapis.com/css2?family=Cinzel:wght@400;500;600&family=Roboto:wght@400;500;700&display=swap" rel="stylesheet">
<style>
:root{
  --blue:#2f72b8;
  --blue-dark:#23599a;
  --navy:#0b1a2e;
  --footer:#0d1a2a;
  --teal:#33b8a4;
  --ink:#1c1c1c;
  --muted:#6b6b6b;
  --line:#e3e3e3;
  --white:#ffffff;
}
*{box-sizing:border-box;margin:0;padding:0}
html,body{width:1200px;height:4093px;overflow:hidden}
body{font-family:"Roboto",Arial,sans-serif;color:var(--ink);background:var(--white);position:relative}
section,header,footer{position:relative;width:1200px}
.abs{position:absolute}
.serif{font-family:"Cinzel",Georgia,serif}

/* hero */
.hero{height:604px;background:linear-gradient(180deg,#0a1830 0%,#10305a 60%,#0c2140 100%);overflow:hidden}
.hero-visual{left:450px;top:120px;width:750px;height:484px;background:radial-gradient(ellipse at 55% 45%,#3aa0e8 0%,#1a5a9c 35%,rgba(12,33,64,0) 70%)}
.hero-city{left:0;top:380px;width:700px;height:224px;background:linear-gradient(180deg,rgba(20,50,90,0) 0%,rgba(20,50,90,.6) 100%)}
.topbar{right:0;top:0;width:720px;height:44px;background:var(--blue);clip-path:polygon(30px 0,100% 0,100% 100%,0 100%);display:flex;align-items:center;padding-left:56px;gap:18px;color:var(--white);font-size:13px}
.topbar .item{display:flex;align-items:center;gap:8px;white-space:nowrap}
.topbar .ic{width:28px;height:28px;border:1.5px solid var(--white);border-radius:50%;display:flex;align-items:center;justify-content:center}
.topbar .phone{font-size:16px;font-weight:700}
.topbar .small{font-size:10px}
.topbar .sep{width:1px;height:28px;background:rgba(255,255,255,.5)}
.flag{width:34px;height:20px;background:#1d3f8a;border:2px solid #fff}
.brand{left:64px;top:12px;width:240px;color:var(--white);text-align:center;white-space:nowrap}
.brand .mark{width:34px;height:34px;border:2px solid var(--white);border-radius:50%;margin:0 auto 6px}
.brand .name{font-size:26px;letter-spacing:1px;line-height:30px}
.brand .sub{font-size:8px;letter-spacing:1px}
.nav{left:518px;top:70px;display:flex;gap:41px;font-size:13px;color:var(--white);font-weight:500;white-space:nowrap}
.hero-title{left:99px;top:240px;font-size:62px;color:var(--white);font-weight:500;letter-spacing:1px;white-space:nowrap}
.hero-text{left:99px;top:324px;width:400px;font-size:13px;line-height:23px;color:var(--white)}
.btn{display:inline-flex;align-items:center;justify-content:center;background:var(--blue);color:var(--white);font-weight:700;border-radius:24px}
.hero-btn{left:99px;top:392px;width:184px;height:46px;font-size:15px}
.dots{left:1124px;top:316px;display:flex;flex-direction:column;gap:12px}
.dots span{width:9px;height:9px;border-radius:50%;background:rgba(255,255,255,.35)}
.dots span:first-child{background:var(--white)}
.down{left:576px;top:578px;width:48px;height:48px;border-radius:50%;background:var(--white);display:flex;align-items:flex-start;justify-content:center;padding-top:10px;z-index:2}

/* headings */
.section-title{font-family:"Cinzel",Georgia,serif;font-weight:500;font-size:42px;text-align:center;color:var(--ink)}
.bar{width:70px;height:3px;background:var(--blue);margin:0 auto}

/* services */
.services{height:1233px;padding-top:95px}
.services .lead{width:640px;margin:28px auto 0;text-align:center;font-size:17px;line-height:29px;color:#444}
.card{position:absolute;width:317px;height:412px;background:var(--white);box-shadow:0 2px 8px rgba(0,0,0,.14);text-align:center}
.card .photo{height:200px}
.card .icon{position:absolute;left:126px;top:168px;width:64px;height:64px;border-radius:50%;background:var(--blue);border:3px solid var(--white);display:flex;align-items:center;justify-content:center}
.card h3{margin-top:58px;font-size:17px;font-weight:500;color:var(--ink);white-space:nowrap}
.card .bar{width:36px;height:2px;margin-top:12px}
.card p{margin:20px auto 0;width:275px;font-size:13px;line-height:21px;color:var(--muted)}

/* about */
.about{height:467px;background:linear-gradient(90deg,#1f5ea6 0%,#3473b7 50%,#2d6bb0 100%);overflow:hidden;color:var(--white)}
.about .ghost{left:-40px;top:160px;font-family:"Roboto",sans-serif;font-weight:700;font-size:110px;color:rgba(255,255,255,.07);transform:rotate(-90deg);transform-origin:center;width:420px}
.about .emblem{left:110px;top:180px;display:flex;align-items:center;gap:22px;color:rgba(255,255,255,.55);font-family:"Cinzel",Georgia,serif;font-size:44px;font-weight:500;letter-spacing:2px;white-space:nowrap}
.about .emblem .dot{width:84px;height:84px;border-radius:50%;border:4px solid rgba(255,255,255,.55);flex:none}
.about h2{left:640px;top:78px;font-family:"Cinzel",Georgia,serif;font-size:42px;font-weight:500;white-space:nowrap}
.about .abar{left:640px;top:140px;width:70px;height:3px;background:var(--white)}
.about h4{left:638px;top:160px;font-size:18px;font-weight:500;white-space:nowrap}
.about p{left:638px;top:196px;width:466px;font-size:14px;line-height:25px}
.about .more{left:638px;top:358px;font-size:15px;font-weight:700;text-decoration:underline;display:flex;align-items:center;gap:6px}

/* posts */
.posts{height:747px;padding-top:78px}
.post-main{left:100px;top:190px;width:482px;height:454px;background:linear-gradient(180deg,#c9c5bd 0%,#8d8680 60%,#3b3735 100%)}
.post-main .date{left:20px;top:328px;height:30px;padding:0 17px;background:var(--blue);color:var(--white);border-radius:15px;font-size:12px;display:flex;align-items:center}
.post-main h3{left:27px;top:370px;width:420px;color:var(--white);font-size:19px;line-height:30px;font-weight:700}
.post{position:absolute;left:601px;width:499px;height:131px;display:flex;gap:18px}
.post .thumb{width:144px;height:130px;border-radius:6px;flex:none}
.post .date{margin-top:18px;font-size:13px;color:var(--teal)}
.post h4{margin-top:14px;font-size:17px;line-height:27px;font-weight:700;width:330px}
.divider{position:absolute;left:601px;width:499px;height:1px;background:var(--line)}

/* contact */
.contact{height:632px;background:linear-gradient(90deg,#f5f5f5 0%,#efefef 55%,#e2e3e4 100%);overflow:hidden}
.contact .desk{right:0;top:120px;width:430px;height:512px;background:linear-gradient(160deg,#b9bcbf 0%,#d8d6d3 55%,#e9e9e9 100%)}
.contact .plant{left:0;top:0;width:150px;height:190px;background:radial-gradient(circle at 30% 30%,#3c7a2d 0%,#5a9a3b 40%,rgba(240,240,240,0) 72%)}
.contact h2{left:100px;top:120px;font-family:"Cinzel",Georgia,serif;font-size:50px;font-weight:500;white-space:nowrap}
.contact .cbar{left:100px;top:180px;width:70px;height:3px;background:var(--blue)}
.contact .lead{left:100px;top:213px;font-size:16px;color:#555}
.field{position:absolute;background:var(--white);border:1px solid #e0e0e0;font-size:13px;color:#666;padding:17px 20px}
.submit{left:100px;top:500px;width:162px;height:48px;font-size:15px;justify-content:flex-start;padding-left:32px;gap:18px}
.submit .plane{position:absolute;right:3px;top:3px;width:42px;height:42px;border-radius:50%;background:var(--white);display:flex;align-items:center;justify-content:center}

/* footer */
.footer{height:410px;background:var(--footer);color:var(--white)}
.f-brand{left:76px;top:90px;width:270px;text-align:center;white-space:nowrap}
.f-brand .mark{width:50px;height:50px;border:2px solid var(--white);border-radius:50%;margin:0 auto 12px}
.f-brand .name{font-family:"Cinzel",Georgia,serif;font-size:30px;line-height:36px;font-weight:500}
.f-brand .sub{font-size:9px;letter-spacing:1px;margin-top:4px}
.socials{left:148px;top:236px;display:flex;gap:14px}
.socials span{width:34px;height:34px;border-radius:50%;background:var(--white)}
.f-col h5{font-size:18px;font-weight:700;margin-bottom:16px}
.f-col li{list-style:none;font-size:14px;line-height:29px;white-space:nowrap}
.f-menu{left:400px;top:82px}
.f-contact{left:585px;top:82px}
.f-contact .row{display:flex;gap:12px;font-size:14px;line-height:22px;margin-bottom:14px;align-items:flex-start}
.f-contact .ic{width:32px;height:32px;border-radius:50%;background:var(--white);flex:none;display:flex;align-items:center;justify-content:center}
.f-services{left:883px;top:82px}
.f-services li{padding-left:22px;position:relative}
.f-services li::before{content:"";position:absolute;left:2px;top:13px;width:4px;height:4px;border-radius:50%;background:var(--white)}
.f-rule{left:100px;top:340px;width:1000px;height:1px;background:rgba(255,255,255,.15)}
.copy{left:0;top:366px;width:1200px;text-align:center;font-size:13px}
</style>
</head>
<body>

<header class="hero">
  <div class="abs hero-city" role="img" aria-label="Night city skyline"></div>
  <div class="abs hero-visual" role="img" aria-label="Hand touching glowing digital data screens"></div>

  <div class="abs topbar">
    <div class="item">
      <span class="ic"><svg width="14" height="14" viewBox="0 0 24 24" fill="#fff"><path d="M6.6 10.8a15.1 15.1 0 0 0 6.6 6.6l2.2-2.2a1 1 0 0 1 1-.25 11.4 11.4 0 0 0 3.6.57 1 1 0 0 1 1 1V20a1 1 0 0 1-1 1A17 17 0 0 1 3 4a1 1 0 0 1 1-1h3.5a1 1 0 0 1 1 1c0 1.25.2 2.45.57 3.570a1 1 0 0 1-.25 1z"/></svg></span>
      <span class="small">CALL US TODAY :</span><span class="phone">555-014-2200</span>
    </div>
    <div class="item">
      <span class="ic"><svg width="14" height="12" viewBox="0 0 24 18" fill="none" stroke="#fff" stroke-width="2"><rect x="1" y="1" width="22" height="16" rx="2"/><path d="M1 2l11 8 11-8"/></svg></span>
      <span>Email: info@k7maplewave.com</span>
    </div>
    <span class="sep"></span>
    <span class="flag" role="img" aria-label="Language flag"></span>
  </div>

  <div class="abs brand">
    <div class="mark"></div>
    <div class="name">K7 MAPLEWAVE</div>
    <div class="sub">CONSULTING GROUP LTD</div>
  </div>

  <nav class="abs nav"><span>Home</span><span>About Us</span><span>Our Services</span><span>News &amp; Events</span><span>Careers</span><span>Contact Us</span></nav>

  <h1 class="abs hero-title serif">K7 MAPLEWAVE</h1>
  <p class="abs hero-text">Lorem ipsum dolor sit amet, consectetur adipiscing elit, sed do eimod tempor incididunt ut labore et dolore magna aliqua.</p>
  <span class="abs btn hero-btn">GET STARTED</span>
  <div class="abs dots"><span></span><span></span><span></span></div>
  <div class="abs down"><svg width="14" height="18" viewBox="0 0 14 18" fill="none" stroke="#2f72b8" stroke-width="2"><path d="M7 1v15M2 11l5 5 5-5"/></svg></div>
</header>

<section class="services">
  <h2 class="section-title">OUR SERVICES</h2>
  <div class="bar" style="margin-top:10px"></div>
  <p class="lead">Lorem ipsum dolor sit amet, consectetur adipiscing elit, sed do eiusmod tempor incididunt ut labore et dolore magna aliqua.</p>

  <div class="card" style="left:99px;top:257px">
    <div class="photo" role="img" aria-label="Calculator, pen and financial charts" style="background:linear-gradient(135deg,#e9eef3,#b8c2cc)"></div>
    <div class="icon"><svg width="30" height="30" viewBox="0 0 24 24" fill="none" stroke="#fff" stroke-width="1.6"><rect x="4" y="3" width="16" height="18" rx="2"/><path d="M7 7h10M7 11h3M12 11h5M7 15h3M12 15h5"/></svg></div>
    <h3>ACCOUNTING</h3><div class="bar"></div>
    <p>Lorem ipsum dolort, consectetur adipiscing elgft, sed do eiusmod or incididunt ut labore et dolore magna aliqua.Lorem ipsum dolort, consectetur adipiscing elit</p>
  </div>
  <div class="card" style="left:442px;top:257px">
    <div class="photo" role="img" aria-label="Woman reviewing documents at a desk" style="background:linear-gradient(135deg,#eceae6,#a9a6a2)"></div>
    <div class="icon"><svg width="30" height="30" viewBox="0 0 24 24" fill="none" stroke="#fff" stroke-width="1.6"><path d="M5 3h11l3 3v15H5z"/><path d="M8 9h8M8 13h8M8 17h5"/></svg></div>
    <h3>BOOK KEEPING</h3><div class="bar"></div>
    <p>Lorem ipsum dolort, consectetur adipiscing elgft, sed do eiusmod or incididunt ut labore et dolore magna aliqua.Lorem ipsum dolort, consectetur adipiscing elit</p>
  </div>
  <div class="card" style="left:783px;top:257px">
    <div class="photo" role="img" aria-label="Businessman working on a laptop with charts" style="background:linear-gradient(135deg,#6e5a44,#d8b58a)"></div>
    <div class="icon"><svg width="30" height="30" viewBox="0 0 24 24" fill="none" stroke="#fff" stroke-width="1.6"><path d="M4 20h16M6 16l4-4 3 3 5-6"/><path d="M15 9h3v3"/></svg></div>
    <h3>FINANCIAL MANAGEMENT</h3><div class="bar"></div>
    <p>Lorem ipsum dolort, consectetur adipiscing elgft, sed do eiusmod or incididunt ut labore et dolore magna aliqua.Lorem ipsum dolort, consectetur adipiscing elit</p>
  </div>
  <div class="card" style="left:99px;top:715px">
    <div class="photo" role="img" aria-label="Document signing across a desk" style="background:linear-gradient(135deg,#4a4038,#cfc6bb)"></div>
    <div class="icon"><svg width="30" height="30" viewBox="0 0 24 24" fill="none" stroke="#fff" stroke-width="1.6"><path d="M3 10l9-6 9 6M5 10v9M9 10v9M15 10v9M19 10v9M3 20h18"/></svg></div>
    <h3>GOVERNMENT GRANTS</h3><div class="bar"></div>
    <p>Lorem ipsum dolort, consectetur adipiscing elgft, sed do eiusmod or incididunt ut labore et dolore magna aliqua.Lorem ipsum dolort, consectetur adipiscing elit</p>
  </div>
  <div class="card" style="left:442px;top:715px">
    <div class="photo" role="img" aria-label="Hand stacking wooden blocks" style="background:linear-gradient(135deg,#d7e6ee,#c9a58a)"></div>
    <div class="icon"><svg width="30" height="30" viewBox="0 0 24 24" fill="none" stroke="#fff" stroke-width="1.6"><circle cx="12" cy="12" r="8"/><circle cx="12" cy="12" r="4"/><path d="M12 2v4M12 18v4M2 12h4M18 12h4"/></svg></div>
    <h3>STRATEGY</h3><div class="bar"></div>
    <p>Lorem ipsum dolort, consectetur adipiscing elgft, sed do eiusmod or incididunt ut labore et dolore magna aliqua.Lorem ipsum dolort, consectetur adipiscing elit</p>
  </div>
  <div class="card" style="left:783px;top:715px">
    <div class="photo" role="img" aria-label="Business handshake over a table" style="background:linear-gradient(135deg,#e7e4df,#8d8173)"></div>
    <div class="icon"><svg width="30" height="30" viewBox="0 0 24 24" fill="none" stroke="#fff" stroke-width="1.6"><circle cx="12" cy="13" r="6"/><path d="M12 10v6M10 11.5h3a1.5 1.5 0 0 1 0 3h-2M4 6l3 2M20 6l-3 2"/></svg></div>
    <h3>MERGERS &amp; ACQUISITIONS</h3><div class="bar"></div>
    <p>Lorem ipsum dolort, consectetur adipiscing elgft, sed do eiusmod or incididunt ut labore et dolore magna aliqua.Lorem ipsum dolort, consectetur adipiscing elit</p>
  </div>
</section>

<section class="about">
  <div class="abs ghost">ABOUT</div>
  <div class="abs emblem"><span class="dot"></span>K7 MAPLEWAVE</div>
  <h2 class="abs">WHO WE ARE?</h2>
  <div class="abs abar"></div>
  <h4 class="abs">K7 MAPLEWAVE CONSULTING GROUP LTD</h4>
  <p class="abs">Lorem ipsum dolor sit amet, consectetur adipiscelit, sed do eiusmod tempor incididunt ut labore et agna aliqua. Quis ipsum suspendisse ultrices gravida. Risus commodo viverra maecenas accumsan lacus vel facilisis. Lorem ipsum dolor sit amet, consectetur adipiscelit, sed do eiusmod tempor incididunt ut labore et agna aliqua. Quis ipsum suspendisse ultrices gravida.</p>
  <span class="abs more">LEARN MORE <svg width="20" height="10" viewBox="0 0 20 10" fill="none" stroke="#fff" stroke-width="1.5"><path d="M0 5h18M14 1l4 4-4 4"/></svg></span>
</section>

<section class="posts">
  <h2 class="section-title">LATEST POSTS</h2>
  <div class="bar" style="margin-top:10px"></div>

  <div class="abs post-main" role="img" aria-label="Woman presenting at a whiteboard to colleagues">
    <span class="abs date">DECEMBER 05,2020</span>
    <h3 class="abs">Lorem ipsum dolor sit amet, consectetur adipiscing elit, sed do eiusmod tempor</h3>
  </div>

  <div class="post" style="top:193px">
    <div class="thumb" role="img" aria-label="Hands working on a laptop" style="background:linear-gradient(135deg,#dfe3e8,#8d96a3)"></div>
    <div><div class="date">DECEMBER 05,2020</div><h4>Lorem ipsum dolor sit ame consectetur adipiscing elit, sed do eiusmod</h4></div>
  </div>
  <div class="divider" style="top:344px"></div>
  <div class="post" style="top:354px">
    <div class="thumb" role="img" aria-label="Aerial city view with finance graphics" style="background:linear-gradient(135deg,#1e4f7e,#6f9cc4)"></div>
    <div><div class="date">DECEMBER 05,2020</div><h4>Lorem ipsum dolor sit ame consectetur adipiscing elit, sed do eiusmod</h4></div>
  </div>
  <div class="divider" style="top:505px"></div>
  <div class="post" style="top:516px">
    <div class="thumb" role="img" aria-label="Financial reports on a desk" style="background:linear-gradient(135deg,#e9e9ea,#9ea3aa)"></div>
    <div><div class="date">DECEMBER 05,2020</div><h4>Lorem ipsum dolor sit ame consectetur adipiscing elit, sed do eiusmod</h4></div>
  </div>
</section>

<section class="contact">
  <div class="abs plant" role="img" aria-label="Green potted plant"></div>
  <div class="abs desk" role="img" aria-label="Laptop on a white desk with folded hands"></div>
  <h2 class="abs">CONTACT US</h2>
  <div class="abs cbar"></div>
  <p class="abs lead">Get in touch set up a complimentary newwork assessment, Today</p>
  <div class="field" style="left:100px;top:256px;width:312px;height:51px">Name*</div>
  <div class="field" style="left:423px;top:256px;width:311px;height:51px">Phone*</div>
  <div class="field" style="left:100px;top:318px;width:312px;height:51px">Email*</div>
  <div class="field" style="left:423px;top:318px;width:311px;height:51px">Company*</div>
  <div class="field" style="left:100px;top:380px;width:634px;height:103px">Comments*</div>
  <span class="abs btn submit">SUMBIT
    <span class="plane"><svg width="20" height="20" viewBox="0 0 24 24" fill="#2f72b8"><path d="M22 2L2 10l7 3 3 7z"/></svg></span>
  </span>
</section>

<footer class="footer">
  <div class="abs f-brand">
    <div class="mark"></div>
    <div class="name">K7 MAPLEWAVE</div>
    <div class="sub">CONSULTING GROUP LTD</div>
  </div>
  <div class="abs socials"><span></span><span></span><span></span></div>

  <div class="abs f-col f-menu">
    <h5>MENU</h5>
    <ul><li>Home</li><li>About Us</li><li>Our Services</li><li>News and Events</li><li>Careers</li><li>Contact Us</li></ul>
  </div>
  <div class="abs f-col f-contact">
    <h5>CONTACT US</h5>
    <div class="row"><span class="ic"><svg width="14" height="16" viewBox="0 0 24 24" fill="#2f72b8"><path d="M12 2a7 7 0 0 0-7 7c0 5 7 13 7 13s7-8 7-13a7 7 0 0 0-7-7zm0 9.5a2.5 2.5 0 1 1 0-5 2.5 2.5 0 0 1 0 5z"/></svg></span><span>4580 Harbor Lane Springfield<br>USA 20415</span></div>
    <div class="row" style="align-items:center"><span class="ic"><svg width="14" height="14" viewBox="0 0 24 24" fill="#2f72b8"><path d="M6.6 10.8a15.1 15.1 0 0 0 6.6 6.6l2.2-2.2a1 1 0 0 1 1-.25 11.4 11.4 0 0 0 3.6.57 1 1 0 0 1 1 1V20a1 1 0 0 1-1 1A17 17 0 0 1 3 4a1 1 0 0 1 1-1h3.5a1 1 0 0 1 1 1c0 1.25.2 2.45.57 3.57a1 1 0 0 1-.25 1z"/></svg></span><span>(555) 014 2200</span></div>
    <div class="row" style="align-items:center"><span class="ic"><svg width="14" height="12" viewBox="0 0 24 18" fill="none" stroke="#2f72b8" stroke-width="2"><rect x="1" y="1" width="22" height="16" rx="2"/><path d="M1 2l11 8 11-8"/></svg></span><span>info@k7maplewave.com</span></div>
  </div>
  <div class="abs f-col f-services">
    <h5>SERVICES</h5>
    <ul><li>Accounting</li><li>Bookkeeping</li><li>Financial Management</li><li>Government Grants</li><li>Strategy</li><li>Mergers and Acquisitions</li><li>Internal Audit (or Assurance)</li></ul>
  </div>
  <div class="abs f-rule"></div>
  <p class="abs copy">© 2021 K7 MAPLEWAVE CONSULTING GROUP LTD . All Rights Reserved.</p>
</footer>

</body>
</html>
```